Business card for a yoga studio
The Reed Yoga Studio
Project: Business card for a yoga studio
Business card for a yoga studio - Health
Creative Brief
Bright & Fun-filled
Lorna Pichet
Owner
27316 Hollin Avenue, Suite 408 Dallas, TX 75219
972-318-YOGA(9642)
lorna@thereedyogastudio.example
TheReedYogaStudio.example
Would like a new/fresh business card design since we have moved. Don't like the dark/heavy feel of the existing card. I would like the phone number to appear as: 972-318-YOGA(9642).
TheReedYogaStudio TheReedYogaStudio
Would like to avoid solid black background or solid dark color background due to the way the cards show wear easily in everyday use/transport, as well as fingerprints.

```html
<!DOCTYPE html>
<html lang="en">
<head>
<meta charset="utf-8">
<title>The Reed Yoga Studio – Business Card</title>
<link rel="stylesheet" href="https://fonts.googleapis.com/css2?family=Open+Sans:wght@400;600;700&display=swap">
<style>
  :root {
    --backdrop: #e9e9ea;
    --ink: #2b2b2b;
    --paper: #ffffff;
    --muted: #666666;
    --back-top: #f7f6f3;
    --back-bottom: #e4e2dd;
    --band: #8f8f8f;
    --pose-area: #bdbab3;
    --shadow: rgba(0,0,0,0.16);
  }
  * { box-sizing: border-box; margin: 0; padding: 0; }
  html, body { width: 1200px; height: 1002px; overflow: hidden; }
  body {
    background: var(--backdrop);
    font-family: "Open Sans", Arial, sans-serif;
    display: flex;
    flex-direction: column;
    align-items: center;
    justify-content: center;
    gap: 32px;
  }
  .card {
    position: relative;
    width: 800px;
    height: 457px;
    border-radius: 26px;
    overflow: hidden;
    box-shadow: 0 6px 18px var(--shadow);
  }

  /* Back side */
  .card-back {
    background: linear-gradient(180deg, var(--back-top), var(--back-bottom));
    color: var(--ink);
  }
  .pose-area {
    position: absolute;
    left: 430px; top: 120px;
    width: 200px; height: 150px;
    border-radius: 10px;
    background: var(--pose-area);
  }
  .back-url {
    position: absolute;
    left: 0; right: 0; top: 318px;
    text-align: center;
    font-size: 21px;
    font-weight: 600;
    letter-spacing: 2px;
  }

  /* Front side */
  .card-front { background: var(--paper); color: var(--ink); }
  .brand {
    position: absolute;
    left: 48px; top: 48px;
    display: flex; align-items: center; gap: 12px;
  }
  .brand-dot { width: 22px; height: 22px; border-radius: 50%; background: var(--band); }
  .brand-name { font-size: 26px; font-weight: 600; letter-spacing: 1px; }
  .contact-list {
    position: absolute;
    left: 48px; top: 150px;
    list-style: none;
    font-size: 15px;
    line-height: 1.25;
  }
  .contact-list li { display: flex; align-items: flex-start; gap: 10px; margin-bottom: 8px; }
  .contact-icon { width: 18px; height: 18px; flex: none; margin-top: 1px; }
  .bottom-band { position: absolute; left: 0; bottom: 0; width: 800px; height: 457px; }
  .front-url {
    position: absolute;
    left: 60px; bottom: 28px;
    color: var(--paper);
    font-size: 19px; font-weight: 600; letter-spacing: 1.5px;
    white-space: nowrap;
  }
  .person {
    position: absolute;
    right: 48px; bottom: 50px;
  }
  .person-name { font-size: 19px; font-weight: 700; }
  .person-role { font-size: 15px; color: var(--muted); }
</style>
</head>
<body>

  <section class="card card-back" aria-label="Card back">
    <div class="pose-area" role="img" aria-label="Yoga pose silhouette artwork"></div>
    <p class="back-url">www.TheReedYogaStudio.example</p>
  </section>

  <section class="card card-front" aria-label="Card front">
    <div class="brand">
      <span class="brand-dot"></span>
      <span class="brand-name">The Reed Yoga Studio</span>
    </div>

    <ul class="contact-list">
      <li>
        <svg class="contact-icon" viewBox="0 0 18 18"><circle cx="9" cy="9" r="9" fill="#8f8f8f"/><path d="M9 4a3 3 0 0 0-3 3c0 2.3 3 6 3 6s3-3.7 3-6a3 3 0 0 0-3-3z" fill="#fff"/><circle cx="9" cy="7" r="1.1" fill="#8f8f8f"/></svg>
        <span>27316 Hollin Avenue, Suite 408<br>Dallas, TX 75219</span>
      </li>
      <li>
        <svg class="contact-icon" viewBox="0 0 18 18"><circle cx="9" cy="9" r="9" fill="#8f8f8f"/><path d="M6 4.5l2 2-1 1.2c.6 1.3 1.6 2.3 2.9 2.9l1.2-1 2 2-1.2 1.6C8.7 13 5 9.3 4.6 5.7z" fill="#fff"/></svg>
        <span>972-318-YOGA(9642)</span>
      </li>
      <li>
        <svg class="contact-icon" viewBox="0 0 18 18"><circle cx="9" cy="9" r="9" fill="#8f8f8f"/><rect x="4.5" y="6" width="9" height="6.5" fill="#fff"/><path d="M4.5 6l4.5 3.6L13.5 6" fill="none" stroke="#8f8f8f" stroke-width="1"/></svg>
        <span>lorna@thereedyogastudio.example</span>
      </li>
      <li>
        <svg class="contact-icon" viewBox="0 0 18 18"><circle cx="9" cy="9" r="9" fill="#8f8f8f"/><circle cx="9" cy="9" r="4.5" fill="none" stroke="#fff" stroke-width="1.2"/><path d="M4.5 9h9M9 4.5c-2 2.5-2 6.5 0 9M9 4.5c2 2.5 2 6.5 0 9" fill="none" stroke="#fff" stroke-width="1"/></svg>
        <span>www.TheReedYogaStudio.example</span>
      </li>
    </ul>

    <svg class="bottom-band" viewBox="0 0 800 457" aria-hidden="true">
      <path d="M0 375 H470 C535 375 540 427 610 427 H800 V457 H0 Z" fill="#8f8f8f"/>
    </svg>
    <p class="front-url">www.TheReedYogaStudio.example</p>

    <div class="person">
      <p class="person-name">Lorna Pichet</p>
      <p class="person-role">Owner</p>
    </div>
  </section>

</body>
</html>
```